"The Craft of Patron Care," fourth edition cover design

Later this year, my publisher, Harold Penmarsh & Daughters, will issue a fourth, substantially revised edition of "The Craft of Patron Care," following the 2016 publication of the third edition and the second and first versions that were issued earlier.

To distinguish this new edition from previous ones, I need a cover design that visually connects and is consistent with what has preceded it, while signaling this is a new and different, worthy of prospective readers/buyers’ attention.

Attached are three different verbal approaches to the new cover; these are NOT MEANT to serve as actual designs, but rather will give you a sense of how language is to be deployed:

The first emphasizes “ART” as the key visual word in the book title;
The second emphasizes “CLIENT SERVICE” as the key visual words in the book title; and,
The third emphasizes just the word "CLIENT" in the book title.

A top-of-the-page is a pre-head that applies to all three versions:
“6 TIMELESS PRINCIPLES FOR ADVERTISING & MARKETING PRO’s
IN AN AI WORLD"

There's a mid-page sub-head for all three versions:
“THE CLASSIC GUIDE,” followed by
“FOURTH EDITION BY GERALD ASHCOMBE

And there's a one-line, bottom-of-the-page designation:
“Foreword by Mae Dunford, Global Executive Creative Director, Starbolt"

The pallette for the previously published third edition was black with red as an accent color on a field of white; I've attached a sample for reference, so you can see how it was executed. For this new fourth edition, I'd like to change the accent color from red to either Wedgewood blue, or British racing green, or an alternative that is assertive and color saturated -- think of primary colors -- that contrast sufficiently with the base of black. As an alternative, you can consider a cover that used either Wedgewood blue, British racing green, or another possibility as a full-bleed field, with copy content either revered out or surprinted.

Lastly, while the new cover largely is meant to be typographically driven, if you can come up with a visual metaphor that illustrates and builds on the book's title, that would be very helpful. By way of reference, the third edition's book cover attempted to do this by introducing a visual element at the end of the book's title that's meant to represent an artist's paint splatter (although I admit it didn't work as well as it should).

Target Market(s)

Prospective purchasers of the book who might discover copies at a bookstore, but more likely will encounter it through online distributors such as Riverdex, Hartwell & Pike, and Tindall’s.

Industry/Entity Type

Advertising and marketing

Font styles to use
Serif
Sans Serif
Other font styles liked:
• A mix of serif and san-serif typefaces is okay. for the examples I shared, I relieid on "Arial Rounded Bold" but you need not be weeded to this. If you opt to mix in a serif font, I am partial to Cambria as a typeface.

Requirements
Must have
• To achieve the goal of being “connected with but distinct” from previous editions, the new cover should be:  Largely typographic, but displaying a color palette different from the previous editions’ black-plus-red-accent on a canvas of white.  Any new accent color selected for use should be vibrant, strong, and highly saturated; think “British racing green,” “Wedgewood blue,” or their equivalents.  In addition to a powerful, “billboard” approach to type and color, consider other visual metaphors that are likely to engage the readers. The winning cover design will stand out from other books, while connecting with the previously published third edition.
Nice to have
• If you can find way to illustrate the book's title through a visual metaphor, that would be ideal.a
Should not have
• Anything that is frivolous or non-sensical

```html
<!DOCTYPE html>
<html lang="en">
<head>
<meta charset="utf-8">
<title>The Craft of Patron Care — Fourth Edition</title>
<link href="https://fonts.googleapis.com/css2?family=Montserrat:wght@500;600;700;800&family=Archivo:wght@800&display=swap" rel="stylesheet">
<style>
  :root {
    --paper: #ffffff;
    --ink: #0a0a0a;
    --racing-green: #1a5e33;
  }
  html, body {
    margin: 0;
    padding: 0;
    overflow: hidden;
    background: var(--paper);
  }
  .cover {
    position: relative;
    width: 927px;
    height: 1200px;
    background: var(--paper);
    font-family: "Montserrat", Arial, sans-serif;
    color: var(--ink);
    overflow: hidden;
  }
  .prehead {
    position: absolute;
    top: 108px;
    left: 0;
    width: 100%;
    margin: 0;
    text-align: center;
    font-weight: 500;
    font-size: 26px;
    line-height: 36px;
    letter-spacing: 0.4px;
  }
  .prehead .accent {
    color: var(--racing-green);
    font-weight: 600;
  }
  .title-block {
    position: absolute;
    top: 270px;
    left: 0;
    width: 927px;
    height: 420px;
  }
  .title-dot { fill: var(--racing-green); }
  .title-lead {
    font-family: "Montserrat", Arial, sans-serif;
    font-weight: 600;
    font-size: 53px;
    fill: var(--ink);
  }
  .title-main {
    font-family: "Archivo", "Montserrat", Arial, sans-serif;
    font-weight: 800;
    font-size: 186px;
    fill: var(--racing-green);
  }
  .edition {
    position: absolute;
    top: 788px;
    left: 0;
    width: 100%;
    text-align: center;
    margin: 0;
  }
  .edition-kicker {
    display: block;
    font-weight: 600;
    font-size: 25px;
    line-height: 32px;
    letter-spacing: 0.3px;
  }
  .edition-number {
    display: block;
    font-weight: 700;
    font-size: 39px;
    line-height: 46px;
    color: var(--racing-green);
    letter-spacing: 0.5px;
  }
  .author {
    position: absolute;
    top: 1034px;
    left: 109px;
    margin: 0;
    font-weight: 700;
    font-size: 28px;
    color: var(--racing-green);
    letter-spacing: 0.4px;
  }
  .foreword {
    position: absolute;
    top: 1073px;
    left: 109px;
    margin: 0;
    font-weight: 500;
    font-size: 16.5px;
    letter-spacing: 0.3px;
  }
</style>
</head>
<body>
  <main class="cover">
    <p class="prehead">
      <span class="accent">6 TIMELESS PRINCIPLES</span> FOR ADVERTISING<br>
      &amp; MARKETING PROS IN AN AI WORLD
    </p>

    <svg class="title-block" viewBox="0 270 927 420" aria-labelledby="book-title">
      <title id="book-title">The Craft of Patron Care</title>
      <circle class="title-dot" cx="253" cy="307" r="26"/>
      <text class="title-lead" x="293" y="352" textLength="335" lengthAdjust="spacingAndGlyphs">THE CRAFT OF</text>
      <text class="title-main" x="172" y="521" textLength="577" lengthAdjust="spacingAndGlyphs">PATRON</text>
      <text class="title-main" x="172" y="667" textLength="577" lengthAdjust="spacingAndGlyphs">CARE</text>
    </svg>

    <p class="edition">
      <span class="edition-kicker">THE CLASSIC GUIDE</span>
      <span class="edition-number">FOURTH EDITION</span>
    </p>

    <p class="author">GERALD ASHCOMBE</p>
    <p class="foreword">FOREWORD BY MAE DUNFORD, GLOBAL EXECUTIVE CREATIVE DIRECTOR, STARBOLT</p>
  </main>
</body>
</html>
```